A reimagined website for a cross-border tax firm

There are two aspects to this project for Brackwell Tax Consultancy:
1) I need a logo update to accommodate increasing focus and specialization in my business. The byline under the name “Brackwell Tax Consultancy” needs to change:
ORIGINAL: FILING AID FOR CIVIC LEDGER PRACTICES
REVISED: CROSS-BORDER TAX SERVICES • U.S. & CANADA
2) I need a website “refresh” (see current website at www.levyhelpdesk.example) based on this logo – a new vision for a website with greater clarity, focus and organization. It should represent a re-envisioning of the current approach, and not the wholesale abandonment of the style represented there. I need it to be creative, compelling and attention grabbing, but still professional. This should, at a minimum, update any places where the old name/logo is used, but I want the redesign to go beyond this to something more intuitive. I need high quality separate PNG files of the various logo styles for use in various documents, but HTML coding would be a helpful but not necessary addition.

Target Market(s)

People in need of cross-border tax services - Canada and US

Coding

Number of Pages Required

Requirements
Must have
• Greater crispness, sharpness - higher resolution
• A more compelling, organized approach - make the wording and images more accessible to the website user (especially the staff bios, which have scroll bars now)
Nice to have
• Replacement of stock image with a true image of the Halifax skyline
Should not have
• Deviate from colour pattern represented in website logo of blue/orange
• Deviate from existing logo except for word replacement

```html
<!DOCTYPE html>
<html lang="en">
<head>
<meta charset="utf-8">
<title>Brackwell Tax Consultancy</title>
<link rel="stylesheet" href="https://fonts.googleapis.com/css2?family=Poppins:wght@400;500;600;700&family=Hind:wght@400;500;600&display=swap">
<style>
:root{
  --cyan:#3fbde6;
  --navy:#2c3f66;
  --ink:#333;
  --muted:#8a8a8a;
  --dark:#222;
  --darker:#1a1a1a;
  --panel:#2b2b2b;
  --light:#f4f4f4;
  --line:#e3e3e3;
  --orange:#e8892b;
  --blue:#1f4d8f;
}
*{box-sizing:border-box;margin:0;padding:0}
html,body{width:1200px;height:2778px;overflow:hidden}
body{font-family:"Hind",Arial,sans-serif;color:var(--ink);background:#fff;position:relative}
.abs{position:absolute}
h1,h2,h3,h4,.btn,.nav a,.poppins{font-family:"Poppins",Arial,sans-serif}

/* hero */
.hero{position:absolute;left:0;top:0;width:1200px;height:644px;
  background:linear-gradient(180deg,#1e2d4f 0%,#304a78 45%,#243a62 100%)}
.hero-photo{position:absolute;inset:0;background:radial-gradient(ellipse at 70% 55%,rgba(120,150,200,.35),transparent 60%)}
.topbar{position:absolute;left:106px;top:0;width:988px;height:40px;display:flex;align-items:center;color:#fff;font-size:13px;gap:30px}
.topbar .item{display:flex;align-items:center;gap:8px}
.topbar .right{margin-left:auto;display:flex;align-items:center;gap:12px}
.dot{width:9px;height:9px;border-radius:50%;background:#fff;display:inline-block}
.lang{background:rgba(255,255,255,.15);padding:4px 10px;display:flex;align-items:center;gap:6px;font-size:12px}
.lang i{width:14px;height:9px;background:#c9d3e6;display:inline-block}
.navbar{position:absolute;left:106px;top:43px;width:988px;height:74px;background:#fff;display:flex;align-items:center}
.brand{padding-left:14px;display:flex;align-items:center;gap:8px}
.brand .mark{width:22px;height:22px;background:var(--blue)}
.brand .name{font-family:"Poppins",sans-serif;font-weight:600;font-size:15px;color:var(--blue);letter-spacing:.3px}
.brand .tag{font-size:8.5px;color:var(--blue);letter-spacing:.6px;margin-top:1px}
.nav{display:flex;gap:30px;margin-left:auto;margin-right:30px;align-items:center}
.nav a{font-size:12px;font-weight:500;color:#222;text-decoration:none}
.quote{width:107px;height:74px;background:var(--cyan);color:#fff;font-size:11.5px;font-weight:600;display:flex;align-items:center;justify-content:center;font-family:"Poppins",sans-serif}
.hero h1{position:absolute;left:94px;top:262px;color:#fff;font-size:46px;line-height:58px;font-weight:700}
.hero p{position:absolute;left:94px;top:390px;color:#fff;font-size:16px;line-height:20px;width:520px}
.btn{position:absolute;height:40px;font-size:11.5px;font-weight:600;color:#fff;display:flex;align-items:center;justify-content:center;text-transform:uppercase}
.btn.outline{left:94px;top:461px;width:138px;border:2px solid #fff}
.btn.fill{left:250px;top:461px;width:124px;background:var(--cyan)}
.arrow{position:absolute;top:320px;width:33px;height:34px;background:rgba(255,255,255,.35);display:flex;align-items:center;justify-content:center}

/* intro */
.center-title{position:absolute;left:0;width:1200px;text-align:center;font-family:"Poppins",sans-serif;font-weight:400;font-size:26px;color:#222}
.rule{position:absolute;height:2px;background:var(--cyan)}
.intro-text{position:absolute;left:260px;top:756px;width:680px;text-align:center;font-size:14.5px;line-height:24px;color:var(--muted)}
.service-img{position:absolute;top:835px;width:313px;height:211px}
.service-card{position:absolute;top:1013px;width:276px;height:137px;background:#fff;border:1px solid #eee;border-top:3px solid var(--cyan);text-align:center;padding:12px 14px 0}
.service-card h3{font-weight:400;font-size:17px;color:#222;margin-bottom:6px}
.service-card p{font-size:13px;line-height:22px;color:var(--muted)}

/* contact */
.dark{position:absolute;left:0;top:1224px;width:1200px;height:400px;background:var(--dark)}
.contact-box{position:absolute;left:106px;top:1283px;width:313px;height:282px;background:var(--panel);padding:28px 26px;color:#fff}
.contact-box h4{font-weight:500;font-size:19px}
.contact-box .sub{font-size:12.5px;line-height:20px;color:#8a8a8a;margin-top:42px}
.cline{display:flex;gap:14px;font-size:13px;line-height:19px;margin-top:14px;color:#e6e6e6}
.cline svg{flex:none;margin-top:2px}
.qcb{position:absolute;left:444px;top:1276px;color:#fff;font-size:27px;font-weight:500;font-family:"Poppins",sans-serif}
.field{position:absolute;width:313px;height:42px;border:1px solid #3a3a3a;background:var(--dark);color:#e0e0e0;font-size:13px;padding:0 14px;display:flex;align-items:center}
.submit{position:absolute;left:444px;top:1502px;width:138px;height:42px;border-radius:21px;background:var(--cyan);color:#fff;font-size:11.5px;font-weight:600;display:flex;align-items:center;justify-content:center;font-family:"Poppins",sans-serif}
.hours{position:absolute;left:606px;top:1514px;color:#e6e6e6;font-size:13px;display:flex;gap:10px;align-items:center}

/* team & faq */
.light{position:absolute;left:0;top:1624px;width:1200px;height:445px;background:var(--light)}
.sec-title{position:absolute;font-family:"Poppins",sans-serif;font-weight:400;font-size:27px;color:#222}
.thin{position:absolute;height:1px;background:var(--line)}
.team-photo{position:absolute;top:1754px;height:242px;background:linear-gradient(180deg,#4a4c50,#2b2c2f)}
.faq-intro{position:absolute;left:613px;top:1748px;width:470px;font-size:12.5px;line-height:21px;color:var(--muted)}
.faq{position:absolute;left:613px;top:1806px;width:481px;height:216px;background:#fff;border:1px solid var(--line)}
.faq .q{position:absolute;left:0;width:479px;display:flex;gap:14px;padding-left:18px;font-size:14px;color:#333;align-items:center}
.faq .q.open{color:var(--cyan)}
.faq .ico{width:24px;height:24px;border-radius:50%;border:1px solid #ccc;display:flex;align-items:center;justify-content:center;color:#bbb;font-size:16px;flex:none}
.faq .q.open .ico{border-color:var(--cyan);color:var(--cyan)}
.faq .a{position:absolute;left:60px;top:52px;width:400px;font-size:12.5px;line-height:21px;color:var(--muted)}

/* partners */
.ctrl{position:absolute;top:2106px;width:28px;height:28px;border:1px solid var(--line);display:flex;align-items:center;justify-content:center}
.partner{position:absolute;top:2182px;width:177px;height:96px;border:1px solid var(--line);display:flex;align-items:center;justify-content:center}
.partner span{width:110px;height:30px;background:#e2e2e2}

/* footer */
.footer{position:absolute;left:0;top:2389px;width:1200px;height:330px;background:var(--dark)}
.fbrand{position:absolute;left:106px;top:2426px;display:flex;align-items:center;gap:8px}
.fbrand .mark{width:22px;height:22px;background:#fff}
.fbrand .name{font-family:"Poppins",sans-serif;font-weight:600;font-size:15px;color:#fff}
.fbrand .tag{font-size:8.5px;color:#fff;letter-spacing:.6px}
.ftext{position:absolute;left:106px;width:390px;font-size:12.5px;line-height:22px;color:#7e7e7e}
.fhead{position:absolute;font-family:"Poppins",sans-serif;font-weight:500;color:#fff;font-size:17px}
.links{position:absolute;left:532px;top:2485px;list-style:none}
.links li{font-size:12.5px;color:#a0a0a0;line-height:30px}
.links li::before{content:"›";margin-right:8px;color:#a0a0a0}
.email{position:absolute;left:710px;top:2518px;width:401px;height:38px;background:#fff;display:flex;align-items:center}
.email .lbl{font-size:12px;color:#777;padding-left:14px;display:flex;gap:12px;align-items:center;letter-spacing:.5px}
.email .send{margin-left:auto;width:35px;height:38px;background:var(--cyan);display:flex;align-items:center;justify-content:center}
.soc{position:absolute;top:2650px;width:32px;height:32px;border-radius:50%;border:1px solid #555}
.bottom{position:absolute;left:0;top:2719px;width:1200px;height:59px;background:var(--darker);color:#8a8a8a;font-size:12.5px}
.bottom .copy{position:absolute;left:106px;top:21px}
.bottom .blinks{position:absolute;right:106px;top:21px;display:flex;gap:34px}
.totop{position:absolute;left:1153px;top:2731px;width:36px;height:36px;border:2px solid var(--cyan);border-radius:4px;display:flex;align-items:center;justify-content:center}
</style>
</head>
<body>

<section class="hero">
  <div class="hero-photo" role="img" aria-label="Business team shaking hands across a meeting table"></div>
  <div class="topbar">
    <div class="item"><svg width="13" height="13" viewBox="0 0 24 24" fill="var(--cyan)"><path d="M6.6 10.8a15 15 0 0 0 6.6 6.6l2.2-2.2a1 1 0 0 1 1-.25 11.4 11.4 0 0 0 3.6.6 1 1 0 0 1 1 1V20a1 1 0 0 1-1 1A17 17 0 0 1 3 4a1 1 0 0 1 1-1h3.5a1 1 0 0 1 1 1c0 1.25.2 2.45.6 3.6a1 1 0 0 1-.25 1z"/></svg>Phone: (555) 014-2290</div>
    <div class="item"><svg width="14" height="11" viewBox="0 0 24 18" fill="var(--cyan)"><path d="M0 0h24v18H0z"/><path d="M0 0l12 9 12-9" stroke="#2c3f66" stroke-width="2" fill="none"/></svg>info@brackwelltax.example</div>
    <div class="right">Stay Connected: <span class="dot"></span><span class="dot"></span><span class="dot"></span><span class="dot"></span>
      <span class="lang"><i></i>English ▾</span></div>
  </div>
  <div class="navbar">
    <div class="brand"><span class="mark"></span><div><div class="name">BRACKWELL TAX CONSULTANCY</div><div class="tag">CROSS-BORDER TAX SERVICES • U.S. &amp; CANADA</div></div></div>
    <nav class="nav"><a>HOME</a><a>OUR TEAM</a><a>FOR INDIVIDUALS</a><a>FOR INDIVIDUALS</a><a>PAYMENT</a>
      <svg width="13" height="13" viewBox="0 0 24 24" fill="none" stroke="#222" stroke-width="3"><circle cx="10" cy="10" r="7"/><path d="M15 15l7 7"/></svg></nav>
    <div class="quote">GET A QUOTE</div>
  </div>
  <div class="arrow" style="left:15px"><svg width="10" height="14" viewBox="0 0 10 14"><path d="M8 1L2 7l6 6" stroke="#fff" stroke-width="2" fill="none"/></svg></div>
  <div class="arrow" style="left:1152px"><svg width="10" height="14" viewBox="0 0 10 14"><path d="M2 1l6 6-6 6" stroke="#fff" stroke-width="2" fill="none"/></svg></div>
  <h1>Looking for first class<br>business plan?</h1>
  <p>With over 10 years of experience helping businesses to find comprehensive solutions.</p>
  <div class="btn outline">Our Company</div>
  <div class="btn fill">Contact Us</div>
</section>

<h2 class="center-title" style="top:688px">Brackwell Tax Consultancy Inc.</h2>
<div class="rule" style="left:570px;top:734px;width:60px;background:#ccc;height:1px"></div>
<p class="intro-text">We are experts in this industry with over 100 years experience. What that means is you are going to get right solution. please find our services.</p>

<div class="service-img" style="left:106px;background:linear-gradient(135deg,#d9d2c4,#8c7c6a)" role="img" aria-label="Colleagues celebrating with a high five in an office"></div>
<div class="service-img" style="left:444px;background:linear-gradient(135deg,#e7e7e2,#9aa19a)" role="img" aria-label="Desk with monitor showing quality control charts"></div>
<div class="service-img" style="left:782px;background:linear-gradient(135deg,#f1e6dc,#c9a692)" role="img" aria-label="Hands typing on a laptop keyboard"></div>
<div class="service-card" style="left:124px"><h3>About Business</h3><p>We have built enviable reputation in all the consumer goods, heavy industry, hightech &amp; manufacturing.</p></div>
<div class="service-card" style="left:462px"><h3>Advanced Analytics</h3><p>Business analytics (BA) is the practice ofiterative, methodical exploration of our organization's data emphasis.</p></div>
<div class="service-card" style="left:800px"><h3>Customer Insigts</h3><p>Customer Insight Analytics solutions delivertargeted and actionable customer analysis that help financial.</p></div>

<section class="dark"></section>
<div class="contact-box">
  <h4>Contact Details</h4>
  <div class="rule" style="left:26px;top:72px;width:40px;height:1px;background:#666"></div>
  <p class="sub">Please find below contact details and contact us today!</p>
  <div class="cline"><svg width="12" height="12" viewBox="0 0 24 24" fill="var(--cyan)"><path d="M6.6 10.8a15 15 0 0 0 6.6 6.6l2.2-2.2a1 1 0 0 1 1-.25 11.4 11.4 0 0 0 3.6.6 1 1 0 0 1 1 1V20a1 1 0 0 1-1 1A17 17 0 0 1 3 4a1 1 0 0 1 1-1h3.5a1 1 0 0 1 1 1c0 1.25.2 2.45.6 3.6a1 1 0 0 1-.25 1z"/></svg>Phone: (555) 014-2290</div>
  <div class="cline"><svg width="13" height="10" viewBox="0 0 24 18" fill="var(--cyan)"><path d="M0 0h24v18H0z"/><path d="M0 0l12 9 12-9" stroke="#2b2b2b" stroke-width="2" fill="none"/></svg>info@brackwelltax.example</div>
  <div class="cline"><svg width="12" height="12" viewBox="0 0 24 24" fill="none" stroke="var(--cyan)" stroke-width="3"><circle cx="12" cy="12" r="9"/><circle cx="12" cy="12" r="2" fill="var(--cyan)"/></svg>418 Harbourline Road, Unit 12<br>Eastport, Nova Scotia B0X 2K7</div>
</div>
<h2 class="qcb">Quick Call Back</h2>
<div class="rule" style="left:444px;top:1324px;width:60px"></div>
<div class="field" style="left:444px;top:1367px">Name *</div>
<div class="field" style="left:782px;top:1367px">Email *</div>
<div class="field" style="left:444px;top:1433px">Ph Num</div>
<div class="field" style="left:782px;top:1433px">Enquiry About<span style="margin-left:auto;font-size:10px">▾</span></div>
<div class="submit">SUBMIT NOW</div>
<div class="hours"><svg width="13" height="13" viewBox="0 0 24 24" fill="none" stroke="var(--cyan)" stroke-width="2.5"><circle cx="12" cy="12" r="10"/><path d="M12 6v6l4 2"/></svg>We are Opened: Monday to Saturday: 9.00am to 16.pm</div>

<section class="light"></section>
<h2 class="sec-title" style="left:106px;top:1660px">Our Team</h2>
<div class="rule" style="left:106px;top:1706px;width:60px"></div>
<div class="thin" style="left:166px;top:1706px;width:422px"></div>
<div class="team-photo" style="left:98px;width:161px" role="img" aria-label="Portrait of a team member in a dark suit"></div>
<div class="team-photo" style="left:265px;width:159px" role="img" aria-label="Portrait of a team member in a dark suit"></div>
<div class="team-photo" style="left:430px;width:161px" role="img" aria-label="Portrait of a team member in a white shirt"></div>

<h2 class="sec-title" style="left:613px;top:1660px">Frequently Asked Questions</h2>
<div class="rule" style="left:613px;top:1706px;width:60px"></div>
<div class="thin" style="left:673px;top:1706px;width:421px"></div>
<p class="faq-intro">These are just some of the most common questions we get asked. For anything else, please contact us – we would be delighted to help.</p>
<div class="faq">
  <div class="q open" style="top:14px"><span class="ico">–</span>What is the procedure to join with your company?</div>
  <p class="a">The master-builder of human happiness one rejects, dislikes sed avoid packages and web page editors now use uncover.</p>
  <div class="thin" style="left:18px;top:126px;width:443px"></div>
  <div class="q" style="top:134px"><span class="ico">+</span>Do you give any offer for premium customer?</div>
  <div class="thin" style="left:18px;top:174px;width:443px"></div>
  <div class="q" style="top:180px"><span class="ico">+</span>What makes you special from others?</div>
</div>

<h2 class="sec-title" style="left:106px;top:2090px">Our Partners</h2>
<div class="rule" style="left:106px;top:2138px;width:60px"></div>
<div class="thin" style="left:166px;top:2138px;width:928px"></div>
<div class="ctrl" style="left:1022px"><svg width="8" height="10" viewBox="0 0 8 10"><path d="M6 1L2 5l4 4" stroke="#999" stroke-width="1.5" fill="none"/></svg></div>
<div class="ctrl" style="left:1064px"><svg width="8" height="10" viewBox="0 0 8 10"><path d="M2 1l4 4-4 4" stroke="#555" stroke-width="1.5" fill="none"/></svg></div>
<div class="partner" style="left:106px"><span></span></div>
<div class="partner" style="left:309px"><span></span></div>
<div class="partner" style="left:513px"><span></span></div>
<div class="partner" style="left:715px"><span></span></div>
<div class="partner" style="left:917px"><span></span></div>

<footer class="footer"></footer>
<div class="fbrand"><span class="mark"></span><div><div class="name">BRACKWELL TAX CONSULTANCY</div><div class="tag">CROSS-BORDER TAX SERVICES • U.S. &amp; CANADA</div></div></div>
<p class="ftext" style="top:2482px">We have built an enviable reputation in the consumer goods, heavy industry, high-tech, manufacturing, medical, recreational vehicle, and transportation sectors. multidisciplinary team of engineering experts.</p>
<p class="ftext" style="top:2566px">Our consulting 20 years of experience we'll ensure you always get the best guidance for our customers.</p>
<h4 class="fhead" style="left:532px;top:2420px">Usefull Links</h4>
<div class="rule" style="left:532px;top:2454px;width:40px;height:1px"></div>
<ul class="links"><li>Business Growth</li><li>Organization</li><li>Advanced Analytics</li><li>Free Consultation</li></ul>
<h4 class="fhead" style="left:710px;top:2420px">Newsletter</h4>
<div class="rule" style="left:710px;top:2454px;width:40px;height:1px"></div>
<p class="ftext" style="left:710px;top:2484px">Sign up today for hints, tips and the latest product news</p>
<div class="email"><span class="lbl"><svg width="12" height="9" viewBox="0 0 24 18" fill="var(--cyan)"><path d="M0 0h24v18H0z"/><path d="M0 0l12 9 12-9" stroke="#fff" stroke-width="2" fill="none"/></svg>Email Address</span>
  <span class="send"><svg width="14" height="14" viewBox="0 0 24 24" fill="#fff"><path d="M2 11L22 2l-9 20-2-8z"/></svg></span></div>
<h4 class="fhead" style="left:710px;top:2586px">Follw Us On</h4>
<div class="rule" style="left:710px;top:2620px;width:40px;height:1px"></div>
<span class="soc" style="left:712px"></span><span class="soc" style="left:752px"></span><span class="soc" style="left:792px"></span><span class="soc" style="left:832px"></span>

<div class="bottom"><span class="copy">Copyright © 2017 Brackwell Tax Consultancy Inc.</span>
  <span class="blinks"><span>Home</span><span>Contact Us</span><span>FAQ's</span></span></div>
<div class="totop"><svg width="20" height="20" viewBox="0 0 24 24"><circle cx="12" cy="12" r="10" fill="var(--cyan)"/><path d="M7 14l5-5 5 5" stroke="#1a1a1a" stroke-width="3" fill="none"/></svg></div>

</body>
</html>
```